The project is a book cover for a health/recipe book for both Kindle and a future soft cover. Title is Morning Orchard Table: Simple Plates for Steady Everyday Living with a subtitle A Month of Brighter Mornings. I am a registed dietitian nutritionist specializing in midlife and senior women to help them look and feel 10 years younger by balancing hormones and curbing inflammationI like the idea of fresh colorful whole foods on the cover with a natural clean look. But I am also open to a cover which expresses vitality--perhaps a woman or couple whose "being" expresses energy and vitality.Since I am unsure right at this moment the exact # of pages for the book, I will need to have some wiggle room in the final stages to get the spine dimensions.I am happy to send a table of contents if that would help.I need to decide on a cover in the next 2 weeks. Below are some ideas on style that I like with reservations. Background on 1 is too dark, 2 is too pastel and 3 is good but doesn't move me as much and my followers liked it the least
Updates
Entered wrong completion date and would like more entries.
Target Market(s)
Woman 40 to 65+, college educated
Industry/Entity Type
Nutrition
Colors
Designer to choose colors to be used in the design.
Look and feel

```html
<!DOCTYPE html>
<html lang="en">
<head>
<meta charset="utf-8">
<title>Morning Orchard Table</title>
<link rel="stylesheet" href="https://fonts.googleapis.com/css2?family=Roboto:wght@400&family=Barlow+Condensed:wght@600&family=Oswald:wght@600&family=Josefin+Sans:wght@400&display=swap">
<style>
  :root {
    --frame: #dcc6c9;
    --marble: #efefee;
    --marble-light: #f8f8f7;
    --marble-shade: #e2e2e1;
    --title-red: #8e1c27;
    --ink: #0c0c0c;
    --produce-red: #d9452e;
    --produce-orange: #f19a2c;
    --produce-green: #5c7d3a;
    --produce-bean: #e9d8c8;
  }
  html, body {
    margin: 0;
    padding: 0;
    width: 750px;
    height: 1200px;
    overflow: hidden;
    background: var(--frame);
  }
  .cover {
    position: relative;
    width: 750px;
    height: 1200px;
    box-sizing: border-box;
    border: 12px solid var(--frame);
    background:
      radial-gradient(ellipse at 30% 55%, var(--marble-light) 0%, transparent 55%),
      radial-gradient(ellipse at 75% 80%, var(--marble-shade) 0%, transparent 60%),
      var(--marble);
    overflow: hidden;
  }
  .produce-photo {
    position: absolute;
    top: 0;
    left: 0;
    width: 726px;
    height: 380px;
    background:
      radial-gradient(ellipse 120px 110px at 75px 180px, var(--produce-red) 0%, transparent 70%),
      radial-gradient(ellipse 90px 100px at 220px 110px, var(--produce-green) 0%, transparent 75%),
      radial-gradient(ellipse 80px 90px at 150px 270px, var(--produce-red) 0%, transparent 70%),
      radial-gradient(ellipse 90px 80px at 460px 110px, var(--produce-orange) 0%, transparent 75%),
      radial-gradient(ellipse 70px 90px at 330px 170px, #f3b62a 0%, transparent 75%),
      radial-gradient(ellipse 60px 60px at 490px 240px, var(--produce-red) 0%, transparent 75%),
      radial-gradient(ellipse 150px 200px at 640px 150px, var(--produce-bean) 0%, transparent 75%),
      linear-gradient(to bottom, rgba(239,239,238,0) 0%, rgba(239,239,238,0) 60%, var(--marble) 100%);
  }
  .title-block {
    position: absolute;
    left: 0;
    right: 0;
    top: 548px;
    text-align: center;
  }
  .main-title {
    margin: 0;
    font-family: "Roboto", sans-serif;
    font-weight: 400;
    font-size: 70px;
    line-height: 0.98;
    color: var(--title-red);
    letter-spacing: -1px;
  }
  .subtitle {
    margin: 16px 0 0;
    font-family: "Barlow Condensed", sans-serif;
    font-weight: 600;
    font-size: 48px;
    line-height: 0.98;
    color: var(--ink);
    letter-spacing: -0.5px;
  }
  .tagline {
    position: absolute;
    left: 31px;
    width: 664px;
    top: 879px;
    height: 52px;
    border-top: 1.5px solid var(--title-red);
    border-bottom: 1.5px solid var(--title-red);
    display: flex;
    align-items: center;
    justify-content: center;
    font-family: "Oswald", sans-serif;
    font-weight: 600;
    font-size: 22px;
    letter-spacing: 0.5em;
    padding-left: 0.5em;
    box-sizing: border-box;
    color: var(--title-red);
    white-space: nowrap;
  }
  .author {
    position: absolute;
    left: 0;
    right: 0;
    top: 1072px;
    text-align: center;
    font-family: "Josefin Sans", sans-serif;
    font-weight: 400;
    font-size: 36px;
    letter-spacing: 0.12em;
    color: var(--ink);
  }
</style>
</head>
<body>
  <div class="cover">
    <div class="produce-photo" role="img" aria-label="Overhead photo of fresh tomatoes, yellow peppers, green beans, rosemary, speckled beans and almonds on white marble"></div>

    <div class="title-block">
      <h1 class="main-title">MORNING ORCHARD<br>TABLE</h1>
      <p class="subtitle">SIMPLE PLATES FOR STEADY<br>EVERYDAY LIVING</p>
    </div>

    <div class="tagline">A MONTH OF BRIGHTER MORNINGS</div>

    <div class="author">HELEN MARSH, RD, MPH</div>
  </div>
</body>
</html>
```